Brisbane IT support business needs our first letterhead (Contest)

Hello we are a Brisbane based Information Technology company providing support and services to small and medium sized businesses. We provide a range of services and solutions.

The business name is Harlowe Network Computing Services, or HNCS for short.

I am looking for a letterhead that looks professional (don't we all want that), but most importantly, it most utilize the colours in the logo attached, and any text used preferably in font type: HandelGotDBol.

```html
<!DOCTYPE html>
<html lang="en">
<head>
<meta charset="utf-8">
<title>HNCS Letterhead</title>
<link rel="stylesheet" href="https://fonts.googleapis.com/css2?family=EB+Garamond:wght@400;600&display=swap">
<style>
  :root {
    --brand-orange: #ec7e27;
    --brand-navy: #114763;
    --paper: #ffffff;
    --backdrop: #e9e6e1;
    --watermark: #eef2f4;
    --ink: #111111;
  }
  * { box-sizing: border-box; margin: 0; padding: 0; }
  html, body {
    width: 1200px;
    height: 900px;
    overflow: hidden;
    background: var(--backdrop);
  }
  .letterhead {
    position: absolute;
    left: 300px;
    top: 26px;
    width: 600px;
    height: 848px;
    background: var(--paper);
    box-shadow: 0 4px 14px rgba(0,0,0,0.25);
    overflow: hidden;
    font-family: "EB Garamond", Georgia, serif;
  }
  .side-swoosh {
    position: absolute;
    left: 0;
    top: 0;
    width: 600px;
    height: 848px;
  }
  .brand {
    position: absolute;
    left: 9px;
    top: 22px;
    display: flex;
    align-items: center;
  }
  .brand-mark {
    width: 102px;
    height: 102px;
    border-radius: 50%;
    background: var(--brand-navy);
    flex: none;
  }
  .brand-divider {
    width: 2px;
    height: 66px;
    background: var(--brand-orange);
    margin: 0 14px 0 16px;
  }
  .brand-text { display: flex; flex-direction: column; }
  .brand-acronym {
    color: var(--brand-orange);
    font-weight: 600;
    font-size: 46px;
    line-height: 0.95;
    letter-spacing: 2px;
  }
  .brand-fullname {
    color: var(--brand-navy);
    font-weight: 600;
    font-size: 10.5px;
    line-height: 1.1;
    text-transform: uppercase;
    letter-spacing: 0.3px;
    max-width: 150px;
  }
  .contact {
    position: absolute;
    right: 26px;
    top: 24px;
    text-align: right;
    color: var(--ink);
    font-size: 21px;
    line-height: 1.12;
    font-style: normal;
  }
  .watermark {
    position: absolute;
    left: 136px;
    top: 277px;
    width: 338px;
    height: 338px;
    border-radius: 50%;
    background: var(--watermark);
  }
</style>
</head>
<body>
  <main class="letterhead">
    <svg class="side-swoosh" viewBox="0 0 600 848" aria-hidden="true">
      <path d="M0 0 H118 C62 40 44 160 58 320 C76 520 118 700 145 848 H0 Z" fill="var(--brand-orange)"/>
    </svg>

    <div class="watermark" aria-hidden="true"></div>

    <header class="brand">
      <div class="brand-mark" aria-hidden="true"></div>
      <div class="brand-divider" aria-hidden="true"></div>
      <div class="brand-text">
        <span class="brand-acronym">HNCS</span>
        <span class="brand-fullname">Harlowe Network Computing Services</span>
      </div>
    </header>

    <address class="contact">
      Sample Street<br>
      Sample Address<br>
      Fax: 123-456-78<br>
      Tel: 123-555-984<br>
      Email: yourname@sample.com
    </address>
  </main>
</body>
</html>
```